Smartphone speedcam App design

We are Dubai based company named QWRN. We are looking design for our Android app. We developed Speed Camera intimation Android app. Our application required GPS/3G to run. The idea is to control over speeding and intimate users the speed camera nearby you.
You can use app while driving. App will intimate you if you crossed road speed limit. App also intimate when speed camera nearby you. For example, Speed camera after 500 meters , 400 meters...etc.

Target Market(s)

UAE market

Industry/Entity Type

It Company

Number of Pages Required

2 page

Requirements
Must have
• my app has option to intimate for speed camera. camera icon/image can appear while intimation only rest of design can show road speed and current driving speed.
• I have attached sample main screen for designer understanding.
Nice to have
• designers can search related apps

```html
<!DOCTYPE html>
<html lang="en">
<head>
<meta charset="utf-8">
<title>VeloWatch – Main Screen</title>
<link rel="stylesheet" href="https://fonts.googleapis.com/css2?family=Roboto:wght@400;500;700&display=swap">
<style>
  :root {
    --status-red: #b9352b;
    --appbar-red: #d8483c;
    --alert-red: #d6362c;
    --needle-red: #d8483c;
    --white: #ffffff;
    --ink: #1b1b1b;
    --label-grey: rgba(190, 190, 190, 0.85);
    --gauge-grey: #d3d3d3;
    --tick-grey: #5a6068;
    --pole-grey: #e6e6e6;
    --bar-dark: #8a8a8a;
    --light-red: #e10d0d;
    --light-green: #1e8c1e;
    --sign-yellow: #f7ea1f;
    --nav-black: #000000;
  }
  * { margin: 0; padding: 0; box-sizing: border-box; }
  html, body { width: 1200px; height: 2564px; overflow: hidden; background: #2a2a2a; }
  body { font-family: "Roboto", Arial, sans-serif; color: var(--ink); }

  .app-screen { position: relative; width: 1200px; height: 2564px; overflow: hidden; }

  .status-bar {
    position: absolute; top: 0; left: 0; width: 1200px; height: 100px;
    background: var(--status-red);
    display: flex; justify-content: flex-end; align-items: center; gap: 22px;
    padding-right: 26px; color: var(--white);
  }
  .status-time { font-size: 46px; font-weight: 500; margin-left: 8px; }

  .app-bar {
    position: absolute; top: 100px; left: 0; width: 1200px; height: 237px;
    background: var(--appbar-red);
    display: flex; justify-content: center; align-items: center;
  }
  .app-name { color: var(--white); font-size: 64px; font-weight: 500; letter-spacing: 0.5px; }
  .settings-button { position: absolute; right: 44px; top: 80px; width: 78px; height: 78px; }

  .road-backdrop {
    position: absolute; top: 337px; left: 0; width: 1200px; height: 2037px;
    background:
      radial-gradient(ellipse 40% 22% at 50% 30%, #c7ccd2 0%, #8a9097 35%, rgba(60,62,66,0) 100%),
      linear-gradient(180deg, #3f4246 0%, #6e7378 30%, #55585c 55%, #3a3b3d 100%);
  }

  .road-name {
    position: absolute; top: 387px; left: 119px; width: 968px; height: 179px;
    background: var(--label-grey);
    display: flex; flex-direction: column; justify-content: center; align-items: center;
  }
  .road-name-title { font-size: 58px; font-weight: 500; line-height: 1.1; }
  .road-name-sub { font-size: 36px; line-height: 1.25; }

  .radar-badge {
    position: absolute; top: 668px; left: 65px; width: 310px; height: 310px;
    border-radius: 50%; background: var(--white);
    display: flex; flex-direction: column; justify-content: center; align-items: center;
  }
  .radar-label { font-size: 40px; font-weight: 500; }
  .radar-distance { font-size: 54px; font-weight: 700; margin-top: 6px; }

  .limit-sign {
    position: absolute; top: 673px; left: 851px; width: 300px; height: 300px;
    border-radius: 50%; background: var(--white);
    border: 30px solid var(--alert-red);
    display: flex; justify-content: center; align-items: center;
  }
  .limit-value { font-size: 72px; font-weight: 700; }

  .signal-bar { position: absolute; top: 666px; left: 404px; width: 404px; height: 43px; background: var(--bar-dark); }
  .signal-box {
    position: absolute; top: 709px; left: 428px; width: 356px; height: 243px;
    background: var(--white);
    display: flex; justify-content: center; align-items: center; gap: 60px;
  }
  .signal-lamp { width: 106px; height: 106px; border-radius: 50%; }
  .signal-lamp.stop { background: var(--light-red); }
  .signal-lamp.go { background: var(--light-green); }
  .signal-pole { position: absolute; top: 952px; left: 580px; width: 56px; height: 380px; background: var(--pole-grey); }

  .speed-gauge { position: absolute; top: 0; left: 0; width: 1200px; height: 2564px; }

  .current-speed { position: absolute; top: 1985px; left: 327px; width: 558px; text-align: center; }
  .current-speed-label { font-size: 54px; font-weight: 500; line-height: 1.2; }
  .current-speed-value { font-size: 100px; font-weight: 700; color: var(--alert-red); line-height: 1.1; }
  .current-speed-unit { font-size: 60px; font-weight: 500; color: var(--ink); }

  .alert-tile {
    position: absolute; top: 2019px; width: 243px; height: 294px;
    background: var(--sign-yellow); border-radius: 12px;
    display: flex; flex-direction: column; align-items: center; justify-content: flex-end;
    padding-bottom: 26px; text-align: center;
  }
  .alert-tile.school { left: 48px; }
  .alert-tile.camera { left: 909px; }
  .alert-tile svg { margin-bottom: 22px; }
  .alert-label { font-size: 27px; font-weight: 700; line-height: 1.25; }

  .nav-bar {
    position: absolute; top: 2374px; left: 0; width: 1200px; height: 190px;
    background: var(--nav-black);
  }
</style>
</head>
<body>
<main class="app-screen">

  <header class="status-bar">
    <svg width="44" height="44" viewBox="0 0 44 44" aria-hidden="true">
      <circle cx="22" cy="24" r="15" fill="none" stroke="#fff" stroke-width="4"/>
      <path d="M22 15 V24 L28 28" fill="none" stroke="#fff" stroke-width="4"/>
      <path d="M5 10 L12 4 M39 10 L32 4" stroke="#fff" stroke-width="4"/>
    </svg>
    <svg width="50" height="40" viewBox="0 0 50 40" aria-hidden="true">
      <path d="M25 38 L1 10 Q25 -8 49 10 Z" fill="#fff"/>
    </svg>
    <svg width="40" height="40" viewBox="0 0 40 40" aria-hidden="true">
      <path d="M38 2 V38 H2 Z" fill="#fff"/>
    </svg>
    <svg width="26" height="46" viewBox="0 0 26 46" aria-hidden="true">
      <rect x="8" y="0" width="10" height="5" fill="#fff"/>
      <rect x="2" y="5" width="22" height="39" fill="none" stroke="#fff" stroke-width="3"/>
      <rect x="2" y="26" width="22" height="18" fill="#fff"/>
    </svg>
    <span class="status-time">16:54</span>
  </header>

  <div class="app-bar">
    <span class="app-name">VeloWatch</span>
    <svg class="settings-button" viewBox="0 0 74 74" aria-label="Settings" role="img">
      <g fill="#fff">
        <circle cx="37" cy="37" r="24"/>
        <rect x="31" y="4" width="12" height="66" rx="3"/>
        <rect x="31" y="4" width="12" height="66" rx="3" transform="rotate(45 37 37)"/>
        <rect x="31" y="4" width="12" height="66" rx="3" transform="rotate(90 37 37)"/>
        <rect x="31" y="4" width="12" height="66" rx="3" transform="rotate(135 37 37)"/>
      </g>
      <circle cx="37" cy="37" r="11" fill="var(--appbar-red)"/>
    </svg>
  </div>

  <div class="road-backdrop" role="img" aria-label="Photo of a lit road tunnel seen from the driver's seat"></div>

  <div class="road-name">
    <div class="road-name-title">Falcon Crest Road</div>
    <div class="road-name-sub">Community Name</div>
  </div>

  <div class="radar-badge">
    <span class="radar-label">RADAR</span>
    <span class="radar-distance">220m</span>
  </div>

  <div class="limit-sign"><span class="limit-value">120</span></div>

  <div class="signal-pole"></div>
  <div class="signal-bar"></div>
  <div class="signal-box">
    <span class="signal-lamp stop"></span>
    <span class="signal-lamp go"></span>
  </div>

  <svg class="speed-gauge" viewBox="0 0 1200 2564" aria-hidden="true">
    <path d="M135 1968 A478 555 0 1 1 1077 1968 Q1000 2035 885 2040 L885 2190 Q885 2270 805 2270 L407 2270 Q327 2270 327 2190 L327 2040 Q212 2035 135 1968 Z" fill="var(--gauge-grey)"/>
    <g stroke="var(--tick-grey)" stroke-width="6" stroke-linecap="round">
      <line x1="606" y1="1325" x2="606" y2="1372"/>
      <line x1="763" y1="1356" x2="750" y2="1401"/>
      <line x1="902" y1="1447" x2="876" y2="1483"/>
      <line x1="1008" y1="1586" x2="973" y2="1611"/>
      <line x1="1067" y1="1758" x2="1027" y2="1768"/>
      <line x1="1073" y1="1944" x2="1032" y2="1938"/>
      <line x1="449" y1="1356" x2="462" y2="1401"/>
      <line x1="310" y1="1447" x2="336" y2="1483"/>
      <line x1="204" y1="1586" x2="239" y2="1611"/>
      <line x1="145" y1="1758" x2="185" y2="1768"/>
      <line x1="139" y1="1944" x2="180" y2="1938"/>
    </g>
    <polygon points="837,1396 644,1890 568,1854" fill="var(--needle-red)"/>
    <circle cx="606" cy="1872" r="78" fill="var(--needle-red)"/>
  </svg>

  <div class="current-speed">
    <div class="current-speed-label">Current speed</div>
    <div class="current-speed-value">140<span class="current-speed-unit">km/h</span></div>
  </div>

  <div class="alert-tile school">
    <svg width="110" height="120" viewBox="0 0 110 120" aria-hidden="true">
      <g fill="#1b1b1b">
        <circle cx="58" cy="14" r="13"/>
        <path d="M46 32 L68 30 L74 64 L90 100 L80 106 L62 72 L50 104 L38 100 L50 64 L44 50 L26 62 L20 54 Z"/>
        <circle cx="20" cy="100" r="14"/>
      </g>
    </svg>
    <span class="alert-label">SCHOOL<br>INTIMATION</span>
  </div>

  <div class="alert-tile camera">
    <svg width="120" height="110" viewBox="0 0 120 110" aria-hidden="true">
      <g fill="#1b1b1b">
        <rect x="4" y="20" width="14" height="84"/>
        <path d="M18 60 H40 V50 H18 Z"/>
        <path d="M36 44 L104 14 L116 42 L48 72 Z"/>
        <rect x="58" y="60" width="16" height="26" transform="rotate(-24 66 73)"/>
      </g>
    </svg>
    <span class="alert-label">RAPORT<br>CAMERA</span>
  </div>

  <nav class="nav-bar" aria-label="System navigation">
    <svg width="1200" height="190" viewBox="0 0 1200 190" aria-hidden="true">
      <polygon points="320,95 370,66 370,124" fill="none" stroke="#fff" stroke-width="6" stroke-linejoin="round"/>
      <circle cx="600" cy="95" r="31" fill="none" stroke="#fff" stroke-width="6"/>
      <rect x="825" y="68" width="54" height="54" fill="none" stroke="#fff" stroke-width="6"/>
    </svg>
  </nav>

</main>
</body>
</html>
```